Marrowfield Contracting Business Cards

Front of card:

Full Logo
Name
Address
Office Phone
Cell Phone
Email
Website

Back:
Logo Mark in background
List and markets and services performed

```html
<!DOCTYPE html>
<html lang="en">
<head>
<meta charset="utf-8">
<title>Marrowfield Contracting Business Cards</title>
<link rel="stylesheet" href="https://fonts.googleapis.com/css2?family=Lato:wght@400;700;900&display=swap">
<style>
  :root {
    --bg: #2a2a2a;
    --red: #d72124;
    --white: #ffffff;
    --grey: #5f5f60;
    --grey-mid: #7a7a7a;
    --grey-light: #e6e6e6;
    --ink: #3c3c3c;
  }
  * { box-sizing: border-box; margin: 0; padding: 0; }
  html, body { width: 1200px; height: 875px; overflow: hidden; }
  body {
    background: var(--bg);
    font-family: "Lato", sans-serif;
    position: relative;
  }
  .card {
    position: absolute;
    width: 525px;
    height: 300px;
    border-radius: 26px;
    overflow: hidden;
    box-shadow: 0 18px 40px rgba(0,0,0,.45);
  }

  /* Back of card */
  .card-back {
    left: 50px; top: 288px;
    background: var(--red);
    color: var(--white);
  }
  .back-brand {
    position: absolute;
    left: 0; top: 0;
    width: 250px; height: 300px;
    display: flex; align-items: center; justify-content: center;
    text-align: center;
    font-weight: 900;
    font-size: 30px;
    line-height: 1.1;
    letter-spacing: .5px;
  }
  .back-divider {
    position: absolute;
    left: 250px; top: 40px;
    width: 1px; height: 220px;
    background: rgba(255,255,255,.75);
    transform: rotate(8deg);
  }
  .services {
    position: absolute;
    left: 290px; top: 50px;
  }
  .services h2 {
    font-weight: 900;
    font-size: 21px;
    letter-spacing: .5px;
    margin-bottom: 8px;
  }
  .services ul { list-style: none; }
  .services li {
    font-size: 14px;
    line-height: 20px;
    padding-left: 16px;
    position: relative;
  }
  .services li::before {
    content: "";
    position: absolute; left: 2px; top: 8px;
    width: 5px; height: 5px; border-radius: 50%;
    background: var(--white);
  }

  /* Front of card */
  .card-front {
    left: 625px; top: 288px;
    background: var(--white);
  }
  .front-band { position: absolute; left: 0; top: 0; }
  .front-brand {
    position: absolute;
    right: 34px; top: 34px;
    display: flex; align-items: center; gap: 12px;
  }
  .brand-dot {
    width: 34px; height: 34px; border-radius: 50%;
    background: var(--red);
  }
  .brand-name {
    color: var(--red);
    font-weight: 900;
    font-size: 22px;
    letter-spacing: .5px;
  }
  .front-rule {
    position: absolute;
    left: 190px; right: 34px; top: 88px;
    height: 1px; background: var(--grey-mid);
  }
  .address {
    position: absolute;
    right: 34px; top: 102px;
    text-align: right;
    font-size: 13px;
    line-height: 18px;
    color: var(--ink);
  }
  .address .company { color: var(--red); }
  .person {
    position: absolute;
    left: 34px; top: 126px;
  }
  .person-name {
    font-weight: 900;
    font-size: 24px;
    color: var(--grey);
    letter-spacing: .3px;
  }
  .person-title {
    font-size: 15px;
    color: var(--red);
    margin-top: 2px;
  }
  .person-rule {
    width: 190px; height: 1px; background: var(--grey-mid);
    margin: 10px 0 8px;
  }
  .contacts { list-style: none; }
  .contacts li {
    display: flex; align-items: center; gap: 10px;
    font-size: 13px; line-height: 19px; color: var(--ink);
  }
  .contacts svg { width: 12px; height: 12px; flex: none; }
  .website {
    position: absolute;
    right: 34px; bottom: 12px;
    color: var(--white);
    font-size: 13px;
    letter-spacing: .3px;
  }
</style>
</head>
<body>

  <section class="card card-back" aria-label="Back of card">
    <div class="back-brand">Marrowfield<br>Contracting</div>
    <div class="back-divider"></div>
    <div class="services">
      <h2>OUR SERVICES</h2>
      <ul>
        <li>Lorem ipsum</li>
        <li>Aliquam tincidunt</li>
        <li>Vestibulum auctor</li>
        <li>Nunc dignissim</li>
        <li>Cras ornare</li>
        <li>Vivamus vestibulum</li>
        <li>Praesent placerat</li>
        <li>Fusce pellentesque</li>
        <li>Integer vitae</li>
      </ul>
    </div>
  </section>

  <section class="card card-front" aria-label="Front of card">
    <svg class="front-band" width="525" height="300" viewBox="0 0 525 300" aria-hidden="true">
      <path d="M0,284 L330,262 C350,260 352,246 372,244 L525,236 L525,244 L376,252 C356,254 354,268 334,270 L0,292 Z" fill="#6a6a6a"/>
      <path d="M0,292 L334,270 C354,268 356,254 376,252 L525,244 L525,300 L0,300 Z" fill="#d72124"/>
    </svg>

    <div class="front-brand">
      <span class="brand-dot"></span>
      <span class="brand-name">Marrowfield Contracting</span>
    </div>
    <div class="front-rule"></div>

    <div class="address">
      <div class="company">Marrowfield Contracting LLC</div>
      <div>Address, City, State</div>
      <div>Country, Zip Code 01235</div>
    </div>

    <div class="person">
      <div class="person-name">DANIEL HARPER</div>
      <div class="person-title">Founder &amp; CEO</div>
      <div class="person-rule"></div>
      <ul class="contacts">
        <li>
          <svg viewBox="0 0 12 12" aria-hidden="true"><path d="M2.5 1 L4.5 1 L5 3.5 L3.8 4.4 C4.4 5.9 6.1 7.6 7.6 8.2 L8.5 7 L11 7.5 L11 9.5 C11 10.3 10.3 11 9.5 11 C5 11 1 7 1 2.5 C1 1.7 1.7 1 2.5 1 Z" fill="#d72124"/></svg>
          (555) 214-3380
        </li>
        <li>
          <svg viewBox="0 0 12 12" aria-hidden="true"><rect x="3" y="0.8" width="6" height="10.4" rx="1.2" fill="none" stroke="#d72124" stroke-width="1.3"/><circle cx="6" cy="9.3" r=".7" fill="#d72124"/></svg>
          (555) 781-0462
        </li>
        <li>
          <svg viewBox="0 0 12 12" aria-hidden="true"><rect x="0.8" y="2.5" width="10.4" height="7" fill="#d72124"/><path d="M1 3 L6 6.8 L11 3" fill="none" stroke="#fff" stroke-width="1"/></svg>
          office@marrowfieldco.com
        </li>
      </ul>
    </div>

    <div class="website">www.marrowfieldco.com</div>
  </section>

</body>
</html>
```